KVT Stationery
KVT - Bright Channel Partners - Media Representatives
Project: KVT Stationery
KVT Stationery - News and Media
Creative Brief
Use same font as used in my logo
Omar Haddine
Regional Sales Director
Sahil Road - Harat El Nour St. Al Jabiya Al Saffa 3 Building - 7th Floor - Office 703-704
o.haddine@kvtgroupco.co
www.kvtgroupco.co
Logos of the media they represent: Lazeezo Oru etc... NB: you will find them here attached

```html
<!DOCTYPE html>
<html lang="en">
<head>
<meta charset="utf-8">
<title>KVT Stationery</title>
<link rel="stylesheet" href="https://fonts.googleapis.com/css2?family=Ubuntu:wght@400;500;700&display=swap">
<style>
  :root {
    --bg: #e9e6e2;
    --orange: #f08a1c;
    --orange-dark: #d9740c;
    --orange-light: #f7a447;
    --grey: #5b5b5b;
    --grey-mid: #8a8a8a;
    --grey-light: #d6d6d6;
    --white: #ffffff;
  }
  * { box-sizing: border-box; margin: 0; padding: 0; }
  html, body { width: 1200px; height: 794px; overflow: hidden; }
  body {
    background: var(--bg);
    font-family: "Ubuntu", sans-serif;
    position: relative;
  }
  .card {
    position: absolute;
    width: 540px;
    height: 310px;
    border-radius: 16px;
    overflow: hidden;
    box-shadow: 0 10px 28px rgba(0,0,0,.18);
  }
  /* front */
  .card-front { left: 40px; top: 150px; background: var(--white); }
  .front-swoosh { position: absolute; inset: 0; }
  .brand { position: absolute; left: 34px; top: 110px; }
  .brand-mark { display: flex; align-items: center; gap: 8px; }
  .brand-dot { width: 22px; height: 22px; border-radius: 50%; background: var(--orange); }
  .brand-name { font-size: 46px; font-weight: 700; color: var(--grey); letter-spacing: 1px; line-height: 1; }
  .brand-full { font-size: 17px; font-weight: 700; color: var(--grey); margin-top: 6px; }
  .brand-tag { font-size: 10px; color: var(--orange); letter-spacing: 3px; margin-top: 3px; text-align: center; }
  .contact { position: absolute; left: 300px; top: 46px; width: 220px; color: var(--grey); }
  .contact-name { font-size: 17px; font-weight: 700; color: var(--orange); }
  .contact-title { font-size: 8px; color: var(--grey-mid); margin-top: 1px; }
  .contact-address { font-size: 7.5px; line-height: 1.5; margin-top: 14px; }
  .contact-list { list-style: none; margin-top: 8px; font-size: 7.5px; line-height: 1.6; }
  .contact-list li { display: flex; align-items: center; gap: 5px; }
  .contact-list .icon { width: 6px; height: 6px; background: var(--orange); border-radius: 1px; }
  /* back */
  .card-back {
    left: 620px; top: 330px;
    background: linear-gradient(160deg, var(--orange-light), var(--orange) 55%, var(--orange-dark));
  }
  .back-brand { position: absolute; top: 40px; left: 0; right: 0; text-align: center; color: var(--white); }
  .back-brand-full { font-size: 30px; font-weight: 700; }
  .back-brand-tag { font-size: 14px; letter-spacing: 4px; margin-top: 2px; }
  .partner-panel {
    position: absolute; left: 100px; top: 145px; width: 340px; height: 130px;
    background: var(--white); border-radius: 4px;
    display: grid; grid-template-columns: repeat(3, 1fr); grid-template-rows: repeat(2, 1fr);
    align-items: center; justify-items: center; padding: 10px;
  }
  .partner-badge { width: 58px; height: 40px; border-radius: 6px; }
  .partner-badge.red { background: #c8282a; }
  .partner-badge.gold { background: #e0a623; border-radius: 50%; width: 52px; height: 36px; }
  .partner-badge.blue { background: #1d5da8; }
  .partner-badge.purple { background: #7a3c98; }
  .partner-badge.teal { background: #2b8fc0; border-radius: 50%; width: 52px; height: 36px; }
  .partner-badge.green { background: #3a8b45; }
</style>
</head>
<body>
  <section class="card card-front" aria-label="Business card front">
    <svg class="front-swoosh" width="540" height="310" viewBox="0 0 540 310" aria-hidden="true">
      <path d="M0 0 H250 C200 60 190 140 240 230 C260 270 280 295 300 310 H0 Z" fill="#f3f3f3"/>
      <path d="M0 250 C90 300 200 300 290 260 C250 300 200 310 170 310 H0 Z" fill="var(--orange)"/>
      <path d="M250 0 C200 60 190 140 240 230 C255 258 270 280 290 300" fill="none" stroke="var(--grey-light)" stroke-width="6"/>
      <path d="M262 0 C215 60 205 140 252 225" fill="none" stroke="var(--orange)" stroke-width="2"/>
    </svg>
    <div class="brand">
      <div class="brand-mark">
        <span class="brand-dot"></span>
        <span class="brand-name">KVT</span>
      </div>
      <div class="brand-full">Bright Channel Partners</div>
      <div class="brand-tag">Media Representatives</div>
    </div>
    <div class="contact">
      <div class="contact-name">Omar Haddine</div>
      <div class="contact-title">Regional Sales Director</div>
      <p class="contact-address">Sahil Road - Harat El Nour St. Al Jabiya<br>Al Saffa 3 Building - 7th Floor<br>Office 703-704</p>
      <ul class="contact-list">
        <li><span class="icon"></span>+000 2 555 0142</li>
        <li><span class="icon"></span>+000 50 555 0187</li>
        <li><span class="icon"></span>+000 2 555 0163</li>
        <li><span class="icon"></span>o.haddine@kvtgroupco.co</li>
        <li><span class="icon"></span>www.kvtgroupco.co</li>
      </ul>
    </div>
  </section>

  <section class="card card-back" aria-label="Business card back">
    <div class="back-brand">
      <div class="back-brand-full">Bright Channel Partners</div>
      <div class="back-brand-tag">Media Representatives</div>
    </div>
    <div class="partner-panel" aria-label="Represented media channels">
      <span class="partner-badge red"></span>
      <span class="partner-badge gold"></span>
      <span class="partner-badge blue"></span>
      <span class="partner-badge purple"></span>
      <span class="partner-badge teal"></span>
      <span class="partner-badge green"></span>
    </div>
  </section>
</body>
</html>
```